Float and wellness centre needs a website refresh

Our float and wellness centre has been operating in Brisbane, Australia for 3 months. Our website is functional and easy to use, but it lacks a compelling visual experience that sells our awesome services to our customers.<br/><br/>We would like a complete redesign of our webpage. It is very important that the redesign considers the page layout for mobile users and the winning design will need to show both a desktop and mobile version of each of the pages listed below.<br/><br/>Out current website can be found at https://www.ebbtidehaven.com.au/<br/><br/>The winning design will need to provide proposals for redesigning the 4 pages listed below:<br/>Home Page - https://www.ebbtidehaven.com.au/<br/>Float Page - https://www.ebbtidehaven.com.au/services/float<br/>Build Gift Card page - https://www.ebbtidehaven.com.au/giftcard/stepone?location=kelsworth<br/>Booking Page - https://www.ebbtidehaven.com.au/Calendar/Day?centerId=kelsworth&selectedCategory=FLOAT&date=12/18/2019%2000:00:00%20+10:00&sessionLength=60<br/><br/>We only need the 4 pages listed above as our web developer will use the assets from the above pages to standardize all the other pages in the site. It is very important your proposed pages contain the same information as our current pages so that we can properly see the complete layout.<br/><br/>The Home page must display the business logo in some way. We would like the website to have a white background and for it make tasteful use of color to highlight key features on the pages. Where color is used it should harmonize with the business logo. The website needs to feel bright, simple and relaxing. Our current site does not use images very well and we have had professional photos taken of the center and the float rooms specifically for this website project. You can download these, and the business logo images here: http://ebbtidehaven.com.au/websiteimages.zip <br/><br/>We have included a few links below to other centers who have pages that we like: <br/><br/>https://www.drifthollowpods.com/ <br/>https://www.quietnook.com.au/ <br/>https://www.moonbaysoak.com.au/<br/>

Industry/Entity Type

Health And Wellness

Number of Pages Required

4 page

Font styles to use
Sans Serif

Colors

Designer to choose colors to be used in the design.

Requirements
Must have
• It is very important your proposed pages contain the same information as our current pages so that we can properly see the complete layout.
• The Home page must display the business logo in some way.
• Where color is used it should harmonize with the business logo.
Nice to have
• The website needs to feel bright, simple and relaxing. Our current site does not use images very well and we have had professional photos taken of the center and the float rooms specifically for this website project. You can download these, and the business logo images here: http://ebbtidehaven.com.au/websiteimages.zip
Should not have
• Dark pages.

```html
<!DOCTYPE html>
<html lang="en">
<head>
<meta charset="utf-8">
<title>Ebbtide Haven</title>
<link href="https://fonts.googleapis.com/css2?family=Lato:wght@300;400;700&family=Montserrat:wght@600;700;800&display=swap" rel="stylesheet">
<style>
:root{
  --teal:#1d8aa4;
  --teal-soft:#6cb7c8;
  --ink:#1b1b1b;
  --text:#555;
  --muted:#777;
  --line:#e6e6e6;
  --footer:#232323;
  --white:#fff;
}
*{box-sizing:border-box;margin:0;padding:0}
html,body{width:1200px;height:3208px;overflow:hidden;background:var(--white)}
body{position:relative;font-family:'Lato',sans-serif;color:var(--text)}
.abs{position:absolute}
a{text-decoration:none;color:inherit}

/* nav */
.site-nav{position:absolute;top:0;left:0;width:1200px;height:78px;background:var(--white);z-index:3}
.site-nav a{position:absolute;top:29px;font-size:16px;font-weight:700;color:var(--ink)}
.site-nav a.active{color:var(--teal)}
.brand-badge{position:absolute;left:543px;top:0;width:154px;height:152px;border-radius:50%;background:var(--white);z-index:4;display:flex;flex-direction:column;align-items:center;justify-content:center;padding-top:30px}
.brand-badge .dot{width:22px;height:22px;border-radius:50%;background:var(--teal);margin-bottom:8px}
.brand-badge .name{font-family:'Lato',sans-serif;font-weight:700;font-size:16px;color:var(--teal);letter-spacing:.5px}

/* hero */
.hero{position:absolute;top:78px;left:0;width:1200px;height:557px;background:linear-gradient(100deg,#d9d3c8 0%,#ece8e1 40%,#f4f3f1 60%,#bfc6c9 100%)}
.hero-title{position:absolute;left:108px;top:258px;font-family:'Montserrat',sans-serif;font-weight:800;font-size:52px;line-height:58px;color:var(--white);text-align:center;text-shadow:0 2px 6px rgba(0,0,0,.35)}
.btn{position:absolute;display:flex;align-items:center;justify-content:center;gap:10px;background:var(--teal);color:var(--white);font-weight:700;font-size:16px}
.btn svg{width:14px;height:14px}
.dots{position:absolute;left:264px;top:543px;display:flex;gap:6px}
.dots span{width:14px;height:14px;border-radius:50%;background:var(--white)}
.dots span.on{background:transparent;border:3px solid var(--white)}

/* gift */
.gift{position:absolute;top:721px;width:478px;height:138px;background:var(--teal-soft)}
.gift .ico{position:absolute;left:80px;top:34px}
.gift h3{position:absolute;left:185px;top:24px;font-size:26px;font-weight:700;color:var(--white)}
.gift .more{position:absolute;left:187px;top:67px;width:150px;height:46px;background:var(--white);color:var(--teal);font-weight:700;font-size:16px;display:flex;align-items:center;justify-content:center;gap:10px}

/* about */
.about-art{position:absolute;left:165px;top:925px;width:255px;height:360px;border-radius:0 180px 180px 0;background:linear-gradient(180deg,#e9eaf0,#c8c9cf)}
.section-title{font-family:'Montserrat',sans-serif;font-weight:800;color:var(--ink);letter-spacing:1px}
.about h2{position:absolute;left:578px;top:955px;font-size:38px}
.about p{position:absolute;left:578px;top:1012px;width:513px;font-size:15.5px;line-height:28.5px;text-align:justify;color:var(--muted)}

/* services */
.services-bg{position:absolute;top:1300px;left:0;width:1200px;height:720px;background:linear-gradient(180deg,#fff 0%,#eef1f4 15%,#e8ecf0 60%,#fff 100%)}
.service{position:absolute;top:1385px;width:240px;text-align:center}
.service .ring{width:96px;height:96px;border-radius:50%;background:var(--white);border:3px solid var(--teal);margin:0 auto;display:flex;align-items:center;justify-content:center;color:var(--teal);box-shadow:0 3px 6px rgba(0,0,0,.12)}
.service h4{margin-top:14px;font-size:23px;font-weight:700;color:var(--ink)}
.service p{margin-top:6px;font-size:15px;line-height:26px;color:var(--muted)}

/* benefits */
.benefits h2{position:absolute;left:0;width:1200px;text-align:center;top:1648px;font-size:38px}
.benefit{position:absolute;width:333px;height:94px;background:var(--white);border-radius:47px;box-shadow:0 2px 10px rgba(0,0,0,.12)}
.benefit .badge{position:absolute;top:10px;width:74px;height:74px;border-radius:50%;background:var(--teal);display:flex;align-items:center;justify-content:center}
.benefit h5{position:absolute;top:20px;font-size:16px;font-weight:700;color:var(--ink)}
.benefit p{position:absolute;top:46px;width:220px;font-size:11px;line-height:19px;color:var(--muted)}
.benefit.left .badge{right:10px}
.benefit.left h5,.benefit.left p{right:105px;text-align:right}
.benefit.right .badge{left:10px}
.benefit.right h5,.benefit.right p{left:105px}
.benefit-pod{position:absolute;left:464px;top:1747px;width:270px;height:270px;border-radius:50%;border:3px solid var(--teal);background:radial-gradient(circle at 50% 48%,#fbfbfb 0%,#e6e7e9 45%,#cfd2cf 80%,#b9bdb8 100%)}

/* mission */
.mission h2{position:absolute;left:0;width:1200px;text-align:center;top:2100px;font-size:38px}
.mission p{position:absolute;left:0;width:1200px;text-align:center;font-size:13.5px;color:var(--muted)}

/* pricing */
.pricing h2{position:absolute;left:0;width:1200px;text-align:center;top:2428px;font-size:38px}
.plan{position:absolute;top:2523px;width:233px;height:303px;background:var(--white);box-shadow:0 2px 12px rgba(0,0,0,.1);text-align:center;overflow:hidden}
.plan h4{margin-top:34px;font-size:21px;font-weight:400;color:var(--ink)}
.plan .sub{margin-top:12px;font-size:12px;color:var(--muted)}
.plan .desc{margin:16px auto 0;width:200px;font-size:12px;line-height:26px;color:var(--muted)}
.plan .price{margin-top:10px;font-size:31px;font-weight:700;color:var(--teal)}
.plan .per{font-size:14px;color:var(--teal);margin-top:2px}
.plan .book{display:inline-block;margin-top:20px;width:106px;height:40px;line-height:36px;border:2px solid var(--teal);color:var(--teal);font-size:13px}
.plan .book.solid{background:var(--teal);color:var(--white);margin-top:16px}
.plan .ribbon{position:absolute;right:0;top:0}

/* footer */
.site-footer{position:absolute;top:2897px;left:0;width:1200px;height:311px;background:var(--footer);color:var(--white)}
.site-footer .brand{position:absolute;left:140px;top:50px;display:flex;align-items:center;gap:10px}
.site-footer .brand .dot{width:20px;height:20px;border-radius:50%;background:var(--teal)}
.site-footer .brand span{font-weight:700;font-size:20px}
.site-footer .blurb{position:absolute;left:140px;top:180px;width:215px;font-size:13px;line-height:26px}
.site-footer h6{position:absolute;top:50px;font-size:17px;font-weight:700}
.site-footer ul{position:absolute;top:82px;list-style:none}
.site-footer li{font-size:16px;height:34.5px}
.site-footer li::before{content:"»";margin-right:14px}
.hours{position:absolute;left:873px;top:50px}
.hours h6{position:static;font-weight:400}
.hours .row{display:flex;font-size:13px;font-weight:700;margin-top:12px}
.hours .row b{width:134px}
.site-footer .rule{position:absolute;left:112px;top:260px;width:976px;height:1px;background:#777}
.site-footer .copy{position:absolute;left:0;width:1200px;top:278px;text-align:center;font-size:15px}
</style>
</head>
<body>

<nav class="site-nav">
  <a class="active" style="left:111px">HOME</a>
  <a style="left:212px">FLOAT</a>
  <a style="left:313px">IR SAUNA</a>
  <a style="left:440px">MHBOT</a>
  <a style="left:730px">BIOMAT</a>
  <a style="left:844px">GIFT CARDS</a>
  <a style="left:986px">CONTACT US</a>
</nav>
<div class="brand-badge"><span class="dot"></span><span class="name">EBBTIDE HAVEN</span></div>

<header class="hero" role="img" aria-label="Photo of a white float pod room with a wooden bench and towels"></header>
<h1 class="hero-title">EBBTIDE<br>HAVEN</h1>
<a class="btn" style="left:235px;top:407px;width:149px;height:46px">BOOK NOW <svg viewBox="0 0 14 14"><circle cx="7" cy="7" r="7" fill="#fff"/><path d="M5.5 4l3 3-3 3" stroke="#1d8aa4" stroke-width="2" fill="none"/></svg></a>
<div class="dots"><span></span><span></span><span class="on"></span><span></span><span></span></div>

<section class="gift" style="left:112px">
  <svg class="ico" width="66" height="70" viewBox="0 0 66 70" fill="none" stroke="#fff" stroke-width="2.5"><rect x="4" y="30" width="58" height="36" rx="3"/><path d="M4 34l29 18 29-18"/><rect x="14" y="6" width="38" height="34"/><path d="M20 16h26M20 24h20"/></svg>
  <h3>BUILD GIFT CARD</h3>
  <a class="more">VIEW MORE <svg width="14" height="14" viewBox="0 0 14 14"><circle cx="7" cy="7" r="7" fill="#1d8aa4"/><path d="M5.5 4l3 3-3 3" stroke="#fff" stroke-width="2" fill="none"/></svg></a>
</section>
<section class="gift" style="left:609px">
  <svg class="ico" width="66" height="70" viewBox="0 0 66 70" fill="none" stroke="#fff" stroke-width="2.5"><rect x="4" y="30" width="58" height="36" rx="3"/><path d="M4 34l29 18 29-18"/><rect x="14" y="6" width="38" height="34"/><path d="M20 16h26M20 24h20"/></svg>
  <h3>REDEEM GIFT CARD</h3>
  <a class="more">VIEW MORE <svg width="14" height="14" viewBox="0 0 14 14"><circle cx="7" cy="7" r="7" fill="#1d8aa4"/><path d="M5.5 4l3 3-3 3" stroke="#fff" stroke-width="2" fill="none"/></svg></a>
</section>

<section class="about">
  <div class="about-art" role="img" aria-label="Photo of the spa reception with plants and a sign board"></div>
  <h2 class="section-title">ABOUT US</h2>
  <p>A floatation tank (float tank) is a dark, soundproof tank which is partially filled with salty water and is heated to outer skin temperature (approximately 35°C). People use floatation tanks for relaxation a practice called flotation therapy. Flotation tanks are often called isolation tanks, sensory deprivation tanks or Restricted Environmental Stimulation Therapy (REST) tank. A floatation tank (float tank) is a dark, soundproof tank which is partially filled with salty water.</p>
  <a class="btn" style="left:578px;top:1228px;width:142px;height:46px">READ MORE <svg viewBox="0 0 14 14"><circle cx="7" cy="7" r="7" fill="#fff"/><path d="M5.5 4l3 3-3 3" stroke="#1d8aa4" stroke-width="2" fill="none"/></svg></a>
</section>

<div class="services-bg" role="img" aria-label="Faded photo of the spa building exterior"></div>
<section class="services">
  <div class="service" style="left:108px"><div class="ring"><svg width="50" height="40" viewBox="0 0 50 40" fill="none" stroke="currentColor" stroke-width="3"><ellipse cx="20" cy="22" rx="17" ry="12"/><path d="M6 22h28"/><circle cx="42" cy="10" r="4"/><path d="M42 16v16"/></svg></div><h4>FLOAT</h4><p>Relax, recharge and replenish.<br>Simple.</p></div>
  <div class="service" style="left:356px"><div class="ring"><svg width="50" height="44" viewBox="0 0 50 44" fill="none" stroke="currentColor" stroke-width="3"><circle cx="25" cy="9" r="5"/><path d="M17 18h16v12H17zM12 32h26M17 32v10M33 32v10M6 8c3 4-3 8 0 12M44 8c3 4-3 8 0 12"/></svg></div><h4>IR SAUNA</h4><p>Turbocharge your detox with<br>our Infrared Sauna.</p></div>
  <div class="service" style="left:602px"><div class="ring"><span style="font-size:44px;font-weight:700">O<sup style="font-size:22px">2</sup></span></div><h4>MHBOT</h4><p>Mild Hyperbaric Oxygen Therapy,<br>oxygen powered healing.</p></div>
  <div class="service" style="left:850px"><div class="ring"><svg width="50" height="44" viewBox="0 0 50 44" fill="none" stroke="currentColor" stroke-width="3"><path d="M4 26h42M8 26v14M42 26v14M14 20h24"/><circle cx="12" cy="18" r="3"/><path d="M18 4c2 3-2 5 0 8M25 4c2 3-2 5 0 8M32 4c2 3-2 5 0 8"/></svg></div><h4>BIOMAT</h4><p>Far Infrared Rays, Negative<br>Ions and Amethyst Crystals.</p></div>
</section>

<section class="benefits">
  <h2 class="section-title">BENEFITS</h2>
  <div class="benefit left" style="left:112px;top:1755px"><h5>WEIGHT LOSS</h5><p>Our infrared saunas promote weight loss by detoxifying the body and burning.</p><div class="badge"><svg width="40" height="40" viewBox="0 0 40 40" fill="none" stroke="#fff" stroke-width="3"><circle cx="24" cy="12" r="7"/><path d="M24 12l3-3M8 38V20h10v18M28 30h8"/></svg></div></div>
  <div class="benefit left" style="left:112px;top:1892px"><h5>PAIN RELIEF</h5><p>Infrared sauna heat penetrates tissue, joints and muscles to relieve.</p><div class="badge"><svg width="40" height="44" viewBox="0 0 40 44" fill="none" stroke="#fff" stroke-width="4" stroke-linecap="round"><circle cx="20" cy="8" r="4" fill="#fff"/><path d="M6 8l14 12 14-12M20 20v10M14 42l6-12 6 12"/></svg></div></div>
  <div class="benefit-pod" role="img" aria-label="Photo of a white oxygen therapy pod"></div>
  <div class="benefit right" style="left:755px;top:1755px"><div class="badge"><svg width="44" height="44" viewBox="0 0 44 44" fill="none" stroke="#fff" stroke-width="3"><path d="M36 14A16 16 0 0 0 8 14M8 30a16 16 0 0 0 28 0M36 6v8h-8M8 38v-8h8"/><path d="M16 28c0-8 6-12 12-12 0 8-6 12-12 12z"/></svg></div><h5>DETOXIFICATION</h5><p>Sweating is good for you. It is the body's safe and natural way.</p></div>
  <div class="benefit right" style="left:755px;top:1892px"><div class="badge"><svg width="44" height="40" viewBox="0 0 44 40" fill="#fff"><circle cx="22" cy="7" r="5"/><path d="M14 16h16l6 10-4 2-4-6v6l8 6H8l8-6v-6l-4 6-4-2z"/></svg></div><h5>RELAXATION</h5><p>Unlike traditional saunas which operate at extremely harsh temperatures.</p></div>
</section>

<section class="mission">
  <h2 class="section-title">OUR MISSION</h2>
  <p style="top:2170px">Our mission is to provide a purpose-built space for our clients to relax, recover and optimise their health.</p>
  <p style="top:2204px">Ebbtide Haven offers Flotation Therapy, Mild Hyperbaric Oxygen Therapy (mHBOT), Infrared Sauna and Biomat sessions.</p>
  <p style="top:2238px">To help us serve and provide real value to our clients we offer membership and bulk booking discounts,</p>
  <p style="top:2272px">as well as great offers in-store</p>
  <a class="btn" style="left:525px;top:2322px;width:150px;height:46px">READ MORE <svg viewBox="0 0 14 14"><circle cx="7" cy="7" r="7" fill="#fff"/><path d="M5.5 4l3 3-3 3" stroke="#1d8aa4" stroke-width="2" fill="none"/></svg></a>
</section>

<section class="pricing">
  <h2 class="section-title">PRICING</h2>
  <div class="plan" style="left:112px"><h4>TANK</h4><div class="sub">60 MIN FLOAT</div><div class="desc">Lorem ipsum dolor sit aconsectetur adipiscing elit, sed do eiusmod.</div><div class="price">$65.00</div><a class="book">BOOK NOW</a></div>
  <div class="plan" style="left:360px"><h4>SAUNA</h4><div class="sub">30 MIN IR</div><div class="desc">Lorem ipsum dolor sit aconsectetur adipiscing elit, sed do eiusmod.</div><div class="price">$40.00</div><a class="book">BOOK NOW</a></div>
  <div class="plan" style="left:607px">
    <svg class="ribbon" width="76" height="78" viewBox="0 0 76 78"><path d="M0 0h76v78z" fill="#1d8aa4"/><text x="55" y="20" fill="#fff" font-family="Lato,sans-serif" font-size="12" font-weight="700" text-anchor="middle">20 %</text><text x="58" y="38" fill="#fff" font-family="Lato,sans-serif" font-size="12" font-weight="700" text-anchor="middle">Off</text></svg>
    <h4>MEMBERSHIP</h4><div class="sub">60 MIN FLOAT</div><div class="desc">Lorem ipsum dolor sit aconsectetur adipiscing elit, sed do eiusmod.</div><div class="price" style="font-size:29px">$25.00</div><div class="per">PER MONTH</div><a class="book solid">BOOK NOW</a></div>
  <div class="plan" style="left:855px"><h4>BIOMAT</h4><div class="sub">45 MIN</div><div class="desc">Lorem ipsum dolor sit aconsectetur adipiscing elit, sed do eiusmod.</div><div class="price">$45.00</div><a class="book">BOOK NOW</a></div>
</section>

<footer class="site-footer">
  <div class="brand"><span class="dot"></span><span>EBBTIDE HAVEN</span></div>
  <p class="blurb">A floatation tank (float tank) is a dark, soundproof tank which is partially.</p>
  <h6 style="left:386px">QUICK LINKS</h6>
  <ul style="left:386px"><li>Home</li><li>About Us</li><li>Benefits</li><li>Bio Mat</li><li>Contact Us</li></ul>
  <h6 style="left:653px">OTHER LINKS</h6>
  <ul style="left:653px"><li>FAQ</li><li>Help Service</li><li>Terms Of Use</li><li>Privacy Policy</li><li>Float</li></ul>
  <div class="hours">
    <h6>OPENING HOURS</h6>
    <div class="row"><b>EARLY SESSIONS</b>: 6AM – 9AM</div>
    <div class="row"><b>NORMAL SESSIONS</b>: 9AM – 5PM</div>
    <div class="row"><b>LATE SESSIONS</b>: 5PM-10PM</div>
  </div>
  <div class="rule"></div>
  <p class="copy">© 2019 Ebbtide Haven. All Rights Reserved</p>
</footer>

</body>
</html>
```